New Stationary Design

Harcourt Electrics Ltd have acquired Brockhurst Catering Equipment Ltd. We will be retaining the Brockhurst Catering Equipment Ltd name and require new letter head, compliment slips & business card designs.

I have attached the existing Harcourt Electrics letterhead to show our current image/brand. I do not wish to change this substantially & imagine maybe a swap of colours from Red logo to Blue, and the title & footer bars maybe in Red. That said, I'm open to subtle changes in the overall design & to maybe modernise it and if we like them, we would probably ask the Designer to update the changes to reflect them on the Harcourt Electrics stationary as well.

We will be able to get some proper high def images for Catering equipment to include, but for the time being if desingers can use any standard stock images for initial presentation.

The logo will be printed onto a Red van so somehow we need to be able to modify it for that use.

Brockhurst Catering Equipment Ltd. Correspondence Address: 47 Lower Fenwick Road, Northampton. NN3 8QS. Tel 01604 738 902. Fax 01604 738 417. No website currently. Registered No: 05817264. Vat No: 481 3306 59. Company Registered Address: 22 Maplin Crescent, Leicester. LE2 7RD. We would also like to mention that we have Regional Service Centres also based in Leicester & Stockport.

Business Cards would be for;

Owen Hartley, Director. owen.hartley@brockhurstcatering-example.co.uk

Steven Pelham, Operations Manager. steven.pelham@brockhurstcatering-example.co.uk

Neil Booth, Service Manager. neil.booth@brockhurstcatering-example.co.uk

Martin Rowley, Business Development Manager. martin.rowley@brockhurstcatering-example.co.uk

We would also like the letter head to include the 'Fuel Guard' logo & our registration Number: To be confirmed. Also the Electrical Contractors logo & the words Wiring Installers Federation underneath so people know what it means. See www.wif-example.co.uk

Target Market(s)

Businesses who use Catering Equipment such as Cookers. fridges etc. Hence, Care Homes, Hospitals, Restaurants etc

Industry/Entity Type

Business

Requirements
Must have
• Resemblance to existing Harcourt Electrics brand, although maybe with some changes & modernisation.
Nice to have
• Could maybe have some 'icons' for the type of equipment we sell instead of photos. Ie Cookers, Ovens, Fridges, Microwaves, Dishwashers, as well as kithen cateringtabling, commercial extraction hoods etc.

```html
<!DOCTYPE html>
<html lang="en">
<head>
<meta charset="utf-8">
<title>Brockhurst Catering Equipment – Letterhead</title>
<link rel="stylesheet" href="https://fonts.googleapis.com/css2?family=Arimo:wght@400;700&family=Pinyon+Script&display=swap">
<style>
  :root {
    --brand-red: #ec1c24;
    --brand-blue: #2b3b9c;
    --ink: #1a1a1a;
    --paper: #ffffff;
    --backdrop: #e9e6e1;
    --badge-fill: #ffe600;
    --badge-edge: #333333;
  }
  * { margin: 0; padding: 0; box-sizing: border-box; }
  html, body {
    width: 1114px; height: 1200px; overflow: hidden;
    background: var(--backdrop);
    font-family: "Arimo", Arial, sans-serif;
    color: var(--ink);
  }
  .letterhead {
    position: absolute; left: 130px; top: 35px;
    width: 852px; height: 1108px;
    background: var(--paper);
    box-shadow: 0 4px 18px rgba(0,0,0,0.18);
    overflow: hidden;
  }
  .header-band {
    position: absolute; left: 0; top: 0; width: 100%; height: 65px;
    background: var(--brand-red);
  }
  .brand {
    position: absolute; left: 31px; top: 26px;
    width: 190px; height: 92px;
    background: var(--paper);
    display: flex; align-items: center; gap: 9px;
    padding-left: 4px;
  }
  .brand-mark {
    flex: 0 0 18px; height: 18px; background: var(--brand-blue);
  }
  .brand-name {
    font-weight: 700; font-size: 21px; line-height: 1.12;
    color: var(--brand-blue);
  }
  .brand-affiliation {
    position: absolute; left: 33px; top: 124px;
    font-size: 11px; font-weight: 700; color: var(--brand-blue);
  }
  .registration {
    position: absolute; left: 530px; top: 51px;
    font-size: 11.5px; color: #fff;
  }
  .registration .label { color: var(--brand-blue); }
  .fuel-guard-badge {
    position: absolute; left: 716px; top: 16px; width: 96px; height: 96px;
  }
  .salutation {
    position: absolute; left: 93px; top: 191px; font-size: 13.5px;
  }
  .letter-body {
    position: absolute; left: 153px; top: 224px; width: 605px;
    font-size: 13.4px; line-height: 17.4px;
  }
  .letter-body p { margin-bottom: 18px; }
  .signature {
    position: absolute; left: 88px; top: 782px;
    font-family: "Pinyon Script", cursive; font-size: 42px; line-height: 1;
  }
  .signatory-title {
    position: absolute; left: 112px; top: 826px; font-size: 13px;
  }
  .footer-band {
    position: absolute; left: 0; bottom: 0; width: 100%; height: 83px;
    background: var(--brand-red); color: #fff;
    text-align: center; font-size: 12.3px; line-height: 20.5px;
    padding-top: 9px;
  }
  .footer-band .label { color: var(--brand-blue); }
  .footer-band .gap { display: inline-block; width: 18px; }
  .footer-band .service-note { font-weight: 700; font-size: 13px; }
</style>
</head>
<body>
<main class="letterhead">
  <div class="header-band"></div>

  <div class="brand">
    <span class="brand-mark"></span>
    <span class="brand-name">Brockhurst Catering<br>Equipment</span>
  </div>
  <div class="brand-affiliation">Wiring Installers Federation</div>

  <div class="registration"><span class="label">Registration No:</span> 00000 000 000</div>

  <svg class="fuel-guard-badge" viewBox="0 0 96 96" role="img" aria-label="Fuel Guard register badge">
    <rect x="1" y="1" width="94" height="94" rx="6" fill="var(--badge-fill)" stroke="var(--badge-edge)" stroke-width="2"/>
  </svg>

  <p class="salutation">Dear Sir / Madam,</p>

  <section class="letter-body">
    <p>Lorem ipsum dolor sit amet, consectetur adipisicing elit, sed do eiusmod tempor labore et olore magna aliqua. Ut enim ad minim veniam, quis nostrud exercitation ullamco laboris nisi ut aliquip ex ea commodo consequa.Lorem ipsum dolor sit amet, nsectetur adipisicing elit, sed do eiusmod tempor incididunt ut labore et dolore magna aliqua. Ut enim ad minim veniam, quis.</p>
    <p>Lorem ipsum dolor sit amet, consectetur adipisicing elit, sed do eiusmod tempor labore et dolore magna aliqua. Ut enim ad minim veniam, quis nostrud exercitation ullamco laboris nisi ut aliquip ex ea commodo consequa.Lorem ipsum dolor sit amet, nsectetur adipisicing elit, sed do eiusmod tempor incididunt ut labore et dolore magna aliqua. Ut enim ad minim veniam, quis.</p>
    <p>Lorem ipsum dolor sit amet, consectetur adipisicing elit, sed do eiusmod tempor labore et dolore magna aliqua. Ut enim ad minim veniam, quis nostrud exercitation ullamco laboris nisi ut aliquip ex ea commodo consequa.Lorem ipsum dolor sit amet, nsectetur adipisicing elit, sed do eiusmod tempor incididunt ut labore et dolore magna aliqua. Ut enim ad minim veniam, quis.</p>
    <p>Lorem ipsum dolor sit amet, consectetur adipisicing elit, sed do eiusmod tempor labore et dolore magna aliqua. Ut enim ad minim veniam, quis nostrud exercitation ullamco laboris nisi ut aliquip ex ea commodo consequa.Lorem ipsum dolor sit amet, nsectetur adipisicing elit, sed do eiusmod tempor incididunt ut labore et dolore magna aliqua. Ut enim ad minim veniam, quis.</p>
    <p>Lorem ipsum dolor sit amet, consectetur adipisicing elit, sed do eiusmod tempor labore et dolore magna aliqua. Ut enim ad minim veniam, quis nostrud exercitation ullamco laboris nisi ut aliquip ex ea commodo consequa.Lorem ipsum dolor sit amet, nsectetur adipisicing elit, sed do eiusmod tempor incididunt ut labore et dolore magna aliqua. Ut enim ad minim veniam, quis.</p>
  </section>

  <div class="signature">Your Name</div>
  <div class="signatory-title">Company Director</div>

  <footer class="footer-band">
    <div><span class="label">Tel:</span> 01604 738 902<span class="gap"></span><span class="label">Fax:</span> 01604 738 417<span class="gap"></span><span class="label">Vat No:</span> 481 3306 59</div>
    <div><span class="label">Correspondence Address:</span> 47 Lower Fenwick Road, Northampton. NN3 8QS<span class="gap"></span><span class="label">Company Registered Address:</span> 22 Maplin Crescent, Leicester. LE2 7RD</div>
    <div class="service-note">We have Regional Service Centres also based in Leicester &amp; Stockport.</div>
  </footer>
</main>
</body>
</html>
```